Website Design - clean, cutting-edge, impressive and lively

We need to upgrade the design (content will stay the same) of our current site: https://brightpage-web.co.il/index.php?lang=en
1. We need a design that is more sophisticated, cutting-edge, and impressive.
2. At the same time, it is important for the site to remain clean and clear (to create feeling of transparency and trust with client).
3. Lastly, the site design must be in line with our logo in its projection of a service that is friendly and sites that are lively.
Target Market(s)
medium-sized businesses, such as VCs, Pharma, and other companies that need brochure-like sites (not ecommerce and not sites dependent on active online marketing).
Industry/Entity Type
Website
Number of Pages Required
2 page
Look and feel
Each slider illustrates characteristics of the customer's brand and the style your logo design should communicate.

```html
<!DOCTYPE html>
<html lang="en">
<head>
<meta charset="utf-8">
<title>BrightPage – Web Design</title>
<link href="https://fonts.googleapis.com/css2?family=Roboto:wght@400;500;700&display=swap" rel="stylesheet">
<style>
:root{
  --purple:#5a2d91;
  --green:#5cb035;
  --red:#f04e23;
  --yellow:#f1b200;
  --text:#444;
  --light:#f0f0f0;
  --mid:#dedede;
  --dark:#2a2a2a;
  --gold:#f5a623;
}
*{box-sizing:border-box;margin:0;padding:0}
html,body{width:1200px;height:4118px;overflow:hidden}
body{position:relative;font-family:'Roboto',sans-serif;color:var(--text);background:#fff}
.abs{position:absolute}
.btn{position:absolute;display:flex;align-items:center;justify-content:center;color:#fff;border-radius:3px;font-size:16px;gap:8px}
.btn-green{background:var(--green)}
.btn-red{background:var(--red)}
.title{position:absolute;color:var(--purple);font-weight:500;font-size:37px}
/* header */
.logo{left:145px;top:36px;display:flex;align-items:center;gap:12px;font-size:44px;font-weight:500;color:var(--purple)}
.logo i{display:block;width:28px;height:28px;background:var(--red)}
.lang{left:934px;top:25px;width:121px;height:40px;border:1px solid #ccc;border-radius:3px;font-size:12px;display:flex;align-items:center;gap:8px;padding-left:12px}
.lang b{width:20px;height:13px;background:#c9cfdc;display:block}
.nav{top:94px;left:541px;display:flex;font-size:15px}
.nav a{color:#333;text-decoration:none;margin-right:40px}
.nav a.active{color:var(--purple)}
/* hero */
.hero{left:0;top:133px;width:1200px;height:481px;
  background:
    radial-gradient(ellipse 260px 200px at 8% 55%,rgba(190,140,120,.85),transparent 70%),
    radial-gradient(ellipse 330px 230px at 38% 58%,#f4f1ec 0,#e2ddd6 55%,transparent 75%),
    radial-gradient(ellipse 120px 140px at 42% 70%,rgba(160,120,95,.7),transparent 70%),
    radial-gradient(ellipse 240px 170px at 82% 18%,rgba(120,90,70,.55),transparent 70%),
    radial-gradient(ellipse 300px 220px at 90% 75%,rgba(236,214,170,.8),transparent 70%),
    radial-gradient(ellipse 260px 200px at 3% 95%,rgba(120,150,210,.7),transparent 70%),
    linear-gradient(100deg,#8e9098 0%,#b9b3ad 25%,#c9c4be 50%,#8f969e 75%,#b7b0a5 100%)}
.hero-arrow{width:45px;height:44px;background:var(--yellow);top:220px;display:flex;align-items:center;justify-content:center}
.hero h2{position:absolute;right:143px;top:160px;text-align:right;color:#fff;font-size:36px;font-weight:500;line-height:42px;text-shadow:0 2px 6px rgba(0,0,0,.45)}
/* welcome */
.welcome-text{left:144px;top:780px;width:410px;font-size:14px;line-height:32px;color:#444}
.welcome-art{left:560px;top:790px;width:640px;height:438px;
  background:
    radial-gradient(ellipse 170px 90px at 78% 82%,#1f3fb0 0,#3353c7 55%,transparent 80%),
    radial-gradient(ellipse 150px 80px at 37% 76%,#2746b8 0,#4a66d2 55%,transparent 80%),
    radial-gradient(ellipse 140px 80px at 62% 45%,#3352c4 0,#5a73d8 55%,transparent 80%),
    radial-gradient(ellipse 90px 60px at 68% 38%,rgba(240,80,90,.7),transparent 75%),
    radial-gradient(ellipse 80px 50px at 45% 28%,rgba(40,170,180,.6),transparent 75%),
    radial-gradient(ellipse 330px 230px at 60% 55%,#d5d8f6 0,#eceefc 60%,transparent 85%),
    #fff}
/* services */
.services-photo{left:0;top:1228px;width:600px;height:934px;
  background:
    radial-gradient(ellipse 200px 150px at 16% 14%,rgba(200,140,50,.85),transparent 75%),
    radial-gradient(ellipse 220px 140px at 22% 70%,rgba(175,125,55,.8),transparent 75%),
    radial-gradient(ellipse 150px 220px at 58% 38%,#1e2226 0,#2c3036 60%,transparent 85%),
    radial-gradient(ellipse 160px 110px at 8% 45%,rgba(225,228,232,.85),transparent 75%),
    radial-gradient(ellipse 260px 150px at 22% 92%,rgba(200,205,212,.8),transparent 75%),
    radial-gradient(ellipse 90px 140px at 90% 85%,rgba(70,140,60,.75),transparent 75%),
    linear-gradient(150deg,#6d8298 0%,#52697f 45%,#3f566d 100%)}
.services-panel{left:600px;top:1228px;width:600px;height:934px;background:var(--light)}
.svc{position:absolute;left:647px;display:flex;align-items:center;gap:25px;font-size:28px;color:#444}
.svc .ico{width:120px;height:120px;border-radius:50%;background:#fff;box-shadow:0 2px 8px rgba(0,0,0,.15);display:flex;align-items:center;justify-content:center}
.svc.on{color:var(--purple)}
.svc.on .ico{background:var(--purple)}
/* projects */
.proj{position:absolute;width:297px}
.proj .ph{height:192px}
.proj p{text-align:center;color:var(--purple);font-size:14.5px;margin-top:12px;text-transform:uppercase}
/* clients */
.clients-bg{left:0;top:2917px;width:600px;height:553px;background:#ececec}
.testi-bg{left:600px;top:2917px;width:600px;height:553px;background:var(--mid)}
.client{position:absolute;width:78px;height:78px;background:#fff;display:flex;align-items:center;justify-content:center;text-align:center;font-size:12px;font-weight:700;color:var(--purple);line-height:14px;padding:4px}
.quote{left:620px;top:3055px;width:435px;height:255px;background:#fff;padding:26px 34px;font-size:11px;line-height:27px;color:#555}
.quote::after{content:"";position:absolute;left:30px;bottom:-14px;border-left:14px solid #fff;border-bottom:14px solid transparent}
.author{left:621px;top:3340px;font-size:15px;line-height:22px;color:var(--purple)}
/* ready */
.ready{top:3540px;width:1200px;text-align:center}
/* footer */
.footer{left:0;top:3755px;width:1200px;height:363px;background:var(--dark)}
.fh{position:absolute;top:3800px;color:var(--gold);font-size:19px;font-weight:500}
.flinks{left:145px;top:3836px;font-size:12px;line-height:27px;color:#bbb}
.fcontact{left:314px;top:3836px;font-size:12px;line-height:27px;color:#bbb}
.fcontact div{display:flex;align-items:center;gap:14px}
.social{position:absolute;top:3936px;width:48px;height:48px;border-radius:50%;border:1px solid #666}
.copy{left:0;top:4063px;width:1200px;text-align:center;font-size:11px;color:#aaa}
</style>
</head>
<body>

<!-- Header -->
<div class="abs logo"><i></i>BrightPage</div>
<div class="btn btn-green" style="left:639px;top:24px;width:159px;height:40px">
  <svg width="14" height="14" viewBox="0 0 24 24"><path fill="#fff" d="M6.6 10.8a15 15 0 0 0 6.6 6.6l2.2-2.2c.3-.3.7-.4 1-.2 1.1.4 2.3.6 3.6.6.6 0 1 .4 1 1V20c0 .6-.4 1-1 1A17 17 0 0 1 3 4c0-.6.4-1 1-1h3.5c.6 0 1 .4 1 1 0 1.3.2 2.5.6 3.6.1.3 0 .7-.2 1z"/></svg>03-555-0148</div>
<div class="btn btn-red" style="left:815px;top:24px;width:104px;height:40px;font-size:14px">Get Quote</div>
<div class="abs lang"><b></b>English<span style="margin-left:10px">▾</span></div>
<nav class="abs nav">
  <a class="active">Services</a><a>Portfolio</a><a>Reviews</a><a>Blog</a><a>About</a><a style="margin-right:0">Contact</a>
</nav>

<!-- Hero -->
<section class="abs hero" role="img" aria-label="Person browsing a fashion shop website on a computer monitor">
  <div class="abs hero-arrow" style="left:55px"><svg width="16" height="20"><path d="M12 2 4 10l8 8" stroke="#222" stroke-width="3" fill="none"/></svg></div>
  <div class="abs hero-arrow" style="left:1099px"><svg width="16" height="20"><path d="M4 2l8 8-8 8" stroke="#222" stroke-width="3" fill="none"/></svg></div>
  <h2>Etiam mattis augue<br>vehicula odio posuere</h2>
  <div class="btn btn-red" style="left:903px;top:260px;width:153px;height:55px;font-size:22px">Get Quote</div>
</section>

<!-- Welcome -->
<h1 class="title" style="left:145px;top:718px">Welcome to BrightPage</h1>
<div class="abs welcome-text">
  <p>Are you looking for a PROFESSIONAL, EXPERIENCED, RELIABLE website company to create a successful online presence for your company?</p>
  <p style="margin-top:32px">For over 20 years, we have been designing, developing, marketing, maintaining and hosting custom-designed, content-driven, technically cutting-edge and easy-to-update sites while providing prompt, personal service.</p>
</div>
<div class="btn btn-red" style="left:144px;top:1060px;width:152px;height:55px;font-size:22px">Get Quote</div>
<div class="abs welcome-art" role="img" aria-label="Isometric illustration of a team working at desks in a blue office"></div>

<!-- Services -->
<div class="abs services-photo" role="img" aria-label="Laptop, tablet and phone showing an architecture studio website"></div>
<div class="abs services-panel"></div>
<h2 class="title" style="left:646px;top:1300px">Services</h2>
<div class="svc on" style="top:1370px"><div class="ico"><svg width="62" height="62" viewBox="0 0 62 62" fill="none" stroke="#fff" stroke-width="2"><rect x="6" y="8" width="50" height="44"/><line x1="6" y1="16" x2="56" y2="16"/><rect x="12" y="22" width="38" height="10"/><rect x="12" y="38" width="9" height="8"/><rect x="26" y="38" width="9" height="8"/><rect x="40" y="38" width="9" height="8"/></svg></div>Website Creation</div>
<div class="svc" style="top:1516px"><div class="ico"><svg width="62" height="62" viewBox="0 0 62 62" fill="none" stroke="#333" stroke-width="2"><rect x="10" y="8" width="42" height="14" rx="2"/><rect x="10" y="24" width="42" height="14" rx="2"/><rect x="10" y="40" width="42" height="14" rx="2"/><circle cx="17" cy="15" r="2"/><circle cx="17" cy="31" r="2"/><circle cx="17" cy="47" r="2"/><line x1="32" y1="15" x2="46" y2="15"/><line x1="32" y1="31" x2="46" y2="31"/><line x1="32" y1="47" x2="46" y2="47"/></svg></div>Website Hosting</div>
<div class="svc" style="top:1662px"><div class="ico"><svg width="62" height="62" viewBox="0 0 62 62" fill="none" stroke="#333" stroke-width="2"><rect x="6" y="8" width="50" height="36" rx="2"/><line x1="31" y1="44" x2="31" y2="52"/><line x1="20" y1="54" x2="42" y2="54"/><line x1="12" y1="18" x2="30" y2="18"/><line x1="12" y1="26" x2="30" y2="26"/><line x1="12" y1="34" x2="30" y2="34"/><rect x="36" y="16" width="14" height="12"/></svg></div>Website Maintenance</div>
<div class="svc" style="top:1808px"><div class="ico"><svg width="62" height="62" viewBox="0 0 62 62" fill="none" stroke="#333" stroke-width="2"><path d="M10 26h10l22-12v34L20 36H10z"/><path d="M16 36l4 14h6l-3-14"/><path d="M48 24q4 7 0 14"/></svg></div>Online Marketing</div>
<div class="svc" style="top:1954px"><div class="ico"><svg width="62" height="62" viewBox="0 0 62 62" fill="none" stroke="#333" stroke-width="2"><path d="M8 26l23-16 23 16v26H8z"/><path d="M8 26l23 16 23-16"/><rect x="18" y="16" width="26" height="18" fill="#fff"/><line x1="22" y1="22" x2="40" y2="22"/><line x1="22" y1="28" x2="36" y2="28"/></svg></div>Newsletter Systems</div>

<!-- Featured projects -->
<h2 class="title" style="left:0;width:1200px;text-align:center;top:2234px">Featured Projects</h2>
<div class="proj" style="left:144px;top:2301px"><div class="ph" role="img" aria-label="Hand signing a document with a pen" style="background:radial-gradient(ellipse at 80% 20%,#1f9dd0,transparent 60%),radial-gradient(ellipse at 40% 70%,#e8e2da,transparent 70%),linear-gradient(120deg,#7fc4d9,#d9dde0 60%,#a8b8bd)"></div><p>Northbay Group International</p></div>
<div class="proj" style="left:451px;top:2301px"><div class="ph" role="img" aria-label="Spoon of yogurt with a strawberry" style="background:radial-gradient(ellipse 50px 40px at 38% 28%,#d8322c,transparent 75%),linear-gradient(180deg,#f6f6f6,#dcdfdf)"></div><p>Milbrook Group</p></div>
<div class="proj" style="left:758px;top:2301px"><div class="ph" role="img" aria-label="City skyline at dusk from a balcony" style="background:linear-gradient(180deg,#4f72ad,#8aa0c4 40%,#c39a6a 70%,#4d4240)"></div><p>Orvion Opportunity Funds</p></div>
<div class="proj" style="left:144px;top:2549px"><div class="ph" role="img" aria-label="Water pouring into cupped hands" style="background:radial-gradient(ellipse at 50% 55%,#d9bfa0,transparent 65%),linear-gradient(160deg,#7f7a72,#a89a85 55%,#5f5a53)"></div><p>Mei Emek</p></div>
<div class="proj" style="left:451px;top:2549px"><div class="ph" role="img" aria-label="Scientist working with laboratory flasks" style="background:radial-gradient(ellipse at 55% 85%,#c2204f,transparent 55%),linear-gradient(160deg,#5f8bc4,#d3dde9 50%,#a33a63)"></div><p>Lenari Pharmaceuticals</p></div>
<div class="proj" style="left:758px;top:2549px"><div class="ph" role="img" aria-label="Portrait of a smiling elderly woman" style="background:linear-gradient(120deg,#2f4f8f 0%,#8a96a6 40%,#d6d6d6 70%,#eee)"></div><p>Friends of Beit Ora</p></div>
<div class="btn btn-green" style="left:548px;top:2798px;width:104px;height:40px;font-size:15px">View All</div>

<!-- Clients & testimonials -->
<div class="abs clients-bg"></div>
<div class="abs testi-bg"></div>
<h2 class="title" style="left:143px;top:2988px;font-size:36px">Some of our valued clients</h2>
<h2 class="title" style="left:621px;top:2988px;font-size:36px">Testimonials</h2>

<div class="client" style="left:144px;top:3055px">Averin</div>
<div class="client" style="left:232px;top:3055px">Domix</div>
<div class="client" style="left:320px;top:3055px">Orvion</div>
<div class="client" style="left:409px;top:3055px">Formel</div>
<div class="client" style="left:497px;top:3055px">Beit Ora</div>
<div class="client" style="left:144px;top:3145px">Tekna</div>
<div class="client" style="left:232px;top:3145px">Hadar Med</div>
<div class="client" style="left:320px;top:3145px">Northbay</div>
<div class="client" style="left:409px;top:3145px">Galim</div>
<div class="client" style="left:497px;top:3145px">Bayit</div>
<div class="client" style="left:144px;top:3232px">Sodana</div>
<div class="client" style="left:232px;top:3232px">Olvani</div>
<div class="client" style="left:320px;top:3232px">Kehila</div>
<div class="client" style="left:409px;top:3232px">Lenari</div>
<div class="client" style="left:497px;top:3232px">Sanvera</div>
<div class="client" style="left:144px;top:3318px">Milbrook</div>
<div class="client" style="left:232px;top:3318px">Roadline</div>
<div class="client" style="left:320px;top:3318px">Verta</div>
<div class="client" style="left:409px;top:3318px">Vidora Pharma</div>
<div class="client" style="left:497px;top:3318px">Global Amuna</div>

<div class="abs quote">"It was a pleasure to work with BrightPage on Orvion's new website. Their ability to understand our unique goals and then create a fluent, comprehensive and clear website design and content to fit is exceptional. Their quick reaction on any feedback we gave enabled us to launch the new website in just three weeks. Overall we felt throughout the project that we were in good hands and had a real partner who took significant responsibility for the success of the project."</div>
<div class="abs author">Dana Levin, Partner,<br>Orvion Opportunity Funds</div>
<div class="btn btn-green" style="left:950px;top:3343px;width:104px;height:40px;font-size:15px">View All</div>

<!-- Ready -->
<div class="abs ready">
  <h2 style="color:var(--purple);font-size:36px;font-weight:500">READY?</h2>
  <p style="font-size:16px;color:#333;margin-top:6px">Tell us about the site you want.</p>
</div>
<div class="btn btn-green" style="left:144px;top:3625px;width:217px;height:48px;font-size:15px">☎ Call +972-3-555-0148</div>
<div class="btn btn-green" style="left:375px;top:3625px;width:217px;height:48px;font-size:15px">✉ Request a Quote</div>
<div class="btn btn-green" style="left:606px;top:3625px;width:217px;height:48px;font-size:15px">✎ Start a Project</div>
<div class="btn btn-green" style="left:837px;top:3625px;width:217px;height:48px;font-size:15px">▣ See our work</div>

<!-- Footer -->
<footer class="abs footer"></footer>
<div class="fh" style="left:145px">Links</div>
<div class="fh" style="left:314px">Contact info</div>
<div class="fh" style="left:720px">Newsletter Sign Up</div>
<div class="abs flinks">Services<br>Portfolio<br>Reviews<br>Blog<br>About<br>Contact</div>
<div class="abs fcontact">
  <div><span>⌖</span>24 HADAR STREET, REHOVOT 7610001 ISRAEL</div>
  <div><span>☎</span>03-555-0148</div>
  <div><span>✉</span>info@brightpage-web.co.il</div>
</div>
<div class="social" style="left:313px"></div>
<div class="social" style="left:377px"></div>
<div class="social" style="left:441px"></div>
<p class="abs" style="left:720px;top:3838px;width:340px;font-size:12px;line-height:18px;color:#bbb">Subscribe to our newsletter to stay informed about ways to optimize your website.</p>
<div class="abs" style="left:720px;top:3890px;width:232px;height:40px;border:1px solid #555;font-size:12px;color:#888;padding:12px 16px">Email Address</div>
<div class="btn btn-green" style="left:950px;top:3890px;width:104px;height:40px;font-size:15px;border-radius:0">Subscribe</div>
<div class="abs" style="left:144px;top:4035px;width:911px;height:1px;background:#444"></div>
<p class="abs copy">Copyright © 2020 BrightPage. All Rights Reserved &nbsp;|&nbsp; Privacy Policy</p>

</body>
</html>
```